E-Commerce startup needs a Shopify store front

3Loom are looking for help designing and building a Shopify store front.

So what do we need?

A simple, user-friendly home page to display menu options and collections of products.

It’s got to be clean. Uncluttered.

No screaming starbursts! No sale countdown timers.

Clean.

Functional. Clean.

Looks great in mobile. Clean.

Clean but not cold. Needs personality. Design should cue trust and quality.

How it will work is this: every update cycle, we’ll add 5 new products to the site. 5 umbrellas, 5 travel mugs, 5 candle holders, etc. We will need a key frame that will hold an image and a headline. We want these frames to feel consistent from one product to the next. It’s important to note that the headlines are key to personality of the site and their treatment should not be overlooked.

Consistent headline style
Consistent background type (solo product or product in-situ)
Consistent branding cues

While these product frames will be the meat of the site, there are other considerations, as well.

When we click on a product key frame, it will take us to a page with that product collection. There will be the 5 products with supporting copy (product details/specs) and images for each. What should this page look like?

What should the header/navigation look like?

What about the footer?

How about the feature image on home/landing page?

How should we handle copy heavy pages (About us, Shipping policy, returns, etc)

Guidelines:
Colour palette to be based on logo but can expand from there.
San-serif fonts
Needs to work across popular devices (mobile/desktop/tablet) and operating systems. With flexibility to expand into an app in the future.

Some multi-category sites we like:

Plomwix.com – Clean header, design and colours feel warm, friendly
Brindlo.com – The rounded feature boxes are cheerful, inviting
Vamo.co.uk – Large images, nice photography, stylish consistent

Some sites we don’t love the look of

Ulko.co.uk – Products photos are too inconsistent in size, shape and style. Looks messy.
Sazo.com – Too many sale offers, pop ups, deals, deals, deals. Feels cheap and desperate.
Frelvin.co.uk – Feels like an overwhelming amount of information and boxes.

Please feel free to contact us with questions.

Thank you for your designs and expertise. Looking forward to seeing your work.

```html
<!DOCTYPE html>
<html lang="en">
<head>
<meta charset="utf-8">
<title>3Loom Storefront – Home Page Concepts</title>
<link rel="stylesheet" href="https://fonts.googleapis.com/css2?family=Poppins:wght@300;400;500;600;700;800&display=swap">
<style>
:root{
  --board:#777777;
  --red:#e93a3a;
  --yellow:#fbb400;
  --yellow-soft:#fbd167;
  --cream:#fdf1d4;
  --cream-light:#fdf6e8;
  --hero-bg:#f8f6f2;
  --footer-bg:#f5f5f5;
  --ink:#111111;
  --white:#ffffff;
}
*{box-sizing:border-box;margin:0;padding:0}
html,body{width:1200px;height:1007px;overflow:hidden}
body{background:var(--board);font-family:"Poppins",sans-serif;color:var(--ink);position:relative}
.page{position:absolute;top:26px;width:552px;background:var(--white);overflow:hidden}
.page--a{left:31px;height:774px}
.page--b{left:616px;height:954px}
.page *{position:absolute}
.page span,.page b,.page em,.page br{position:static}

/* header */
.brand{font-weight:800;font-size:30px;letter-spacing:-0.5px;color:var(--red);line-height:1}
.site-header .brand{left:52px;top:8px}
.search{left:175px;top:14px;width:211px;height:18px;border:1px solid var(--red);border-radius:10px;font-size:5.5px;line-height:16px;padding-left:7px;color:var(--ink)}
.search svg{right:7px;top:3px}
.account{left:407px;top:20px;font-size:5px;font-weight:500;white-space:nowrap}
.account-icon{left:473px;top:18px}
.bag-icon{left:493px;top:18px}
.nav{left:0;top:43px;width:552px;height:21px;background:var(--red);display:flex;padding-left:86px}
.nav a{position:static;color:var(--white);font-size:5.2px;font-weight:500;line-height:21px;text-decoration:none;margin-right:23px}

/* hero */
.hero{left:0;top:64px;width:552px;height:267px;background:var(--hero-bg)}
.hero-card{left:22px;top:31px;width:296px;height:197px;background:var(--cream);border-radius:12px;overflow:hidden}
.hero-photo{left:190px;top:0;width:106px;height:197px;background:linear-gradient(180deg,rgba(253,241,212,0) 0%,#c9d3a4 45%,#dfe4dc 75%,#e8ebe6 100%)}
.hero-title{left:28px;top:35px;font-size:17px;font-weight:700;line-height:25px;text-transform:uppercase;white-space:nowrap}
.hero-title em{font-style:normal;color:var(--red)}
.hero-btn{left:30px;top:122px;width:63px;height:22px;background:var(--yellow);font-size:7px;font-weight:700;text-align:center;line-height:22px}
.tile{width:95px;height:96px;border-radius:4px}
.tile.t1{left:326px;top:34px;background:linear-gradient(180deg,var(--cream) 0%,#c3cf9c 55%,#ece6d6 100%)}
.tile.t2{left:430px;top:34px;background:linear-gradient(180deg,#ecebe6 0%,#a9bd86 55%,#d8c9b0 100%)}
.tile.t3{left:326px;top:135px;background:linear-gradient(180deg,#eeeeee 0%,#b6c49c 55%,#f4f4f4 100%)}
.tile.t4{left:430px;top:135px;background:linear-gradient(180deg,var(--cream) 0%,#a8bd84 55%,#e8e0cd 100%)}

/* recent additions – layout a */
.section-title{font-size:18px;font-weight:800;text-transform:uppercase;white-space:nowrap}
.page--a .section-title{left:52px;top:364px}
.pager{top:369px}
.pager.prev{left:283px}
.pager.next{left:296px}
.mini-card{top:400px;width:84px;height:120px;background:var(--cream-light);border-radius:4px}
.mini-card.c1{left:49px}.mini-card.c2{left:138px;background:var(--yellow-soft)}.mini-card.c3{left:226px}
.mini-img{left:10px;top:12px;width:64px;height:58px;border-radius:4px}
.c1 .mini-img{background:linear-gradient(135deg,#f3efe6 0%,#9a9a9a 100%)}
.c2 .mini-img{background:linear-gradient(180deg,#f0c860 0%,#c9a94b 100%)}
.c3 .mini-img{background:linear-gradient(180deg,#f6efe2 0%,#8a8a86 100%)}
.mini-text{left:9px;top:85px;width:70px;font-size:4.8px;font-weight:500;line-height:8px}
.c2 .mini-text{color:#8a6a20;font-weight:400}
.quick-view{left:20px;top:34px;width:44px;height:11px;border-radius:6px;background:var(--white);color:var(--yellow);font-size:4.5px;text-align:center;line-height:11px}
.quick-cart{left:19px;top:51px;width:46px;height:11px;border-radius:6px;background:var(--red);color:var(--white);font-size:4.5px;font-weight:600;text-align:center;line-height:11px}
.view-more{left:52px;top:538px;width:74px;height:21px;border-radius:11px;background:var(--yellow);font-size:7.5px;font-weight:600;text-align:center;line-height:21px;text-transform:uppercase}
.flash{left:326px;top:367px;width:175px;height:196px;background:var(--red)}
.flash-img{left:10px;top:10px;width:155px;height:125px;border-radius:4px;background:linear-gradient(135deg,#d8514d 0%,#b93431 100%)}
.flash-title{left:14px;top:146px;color:var(--white);font-size:14.5px;font-weight:600}
.flash-sub{left:14px;top:167px;color:var(--yellow);font-size:8px;font-weight:600}

/* recent additions – layout b */
.page--b .section-title{left:0;width:552px;text-align:center;top:368px}
.feature{top:405px;width:142px;height:188px;border-radius:5px;overflow:hidden}
.feature.f1{left:51px;background:linear-gradient(180deg,#d9dbdc 0%,#e6e8e8 45%,#6d6f70 100%)}
.feature.f2{left:204px;background:linear-gradient(180deg,#e4e5e6 0%,#9c6a72 50%,#5e6062 100%)}
.feature.f3{left:358px;background:linear-gradient(180deg,#ececec 0%,#c9a3c8 45%,#595b5d 100%)}
.feature-title{left:11px;bottom:11px;width:125px;color:var(--white);font-size:10px;font-weight:700;line-height:16px}
.feature-arrow{top:488px;width:18px;height:18px;border-radius:50%;background:var(--yellow)}
.feature-arrow svg{left:5px;top:4px}
.feature-arrow.left{left:25px}.feature-arrow.right{left:509px}
.arrivals{left:51px;top:604px;width:449px;height:146px;background:var(--red);border-radius:3px;overflow:hidden}
.arrivals-img{left:0;top:0;width:187px;height:146px;background:linear-gradient(135deg,#8a5a22 0%,#c98a3c 50%,#3a3a44 100%)}
.arrivals-title{left:214px;top:16px;color:var(--white);font-size:16.5px;font-weight:700}
.arrivals-sub{left:214px;top:38px;color:var(--yellow);font-size:4.2px;font-weight:700}
.arrivals-copy{left:214px;top:50px;width:200px;color:var(--white);font-size:5.8px;line-height:13.7px}
.arrivals-btn{left:215px;top:108px;width:55px;height:19px;background:var(--yellow);font-size:5.8px;font-weight:700;text-align:center;line-height:19px}

/* footer */
.site-footer{left:0;width:552px;height:136px;background:var(--footer-bg)}
.page--a .site-footer{top:610px}
.page--b .site-footer{top:790px}
.site-footer .brand{left:0;width:552px;text-align:center;top:41px;font-size:24px}
.footer-links{left:0;width:552px;top:77px;text-align:center;font-size:6.8px;font-weight:300;color:var(--ink);white-space:nowrap}
.footer-links span{margin:0 4px}
.socials{left:227px;top:100px;display:flex;gap:3px}
.socials i{position:static;display:block;width:17px;height:17px;border:1px solid var(--yellow);border-radius:50%}
.copyright{left:0;width:552px;height:28px;background:var(--red);color:var(--white);font-size:6.8px;font-weight:300;text-align:center;line-height:28px}
.page--a .copyright{top:746px}
.page--b .copyright{top:926px}
</style>
</head>
<body>

<!-- Layout A -->
<section class="page page--a">
  <header class="site-header">
    <div class="brand">3Loom</div>
    <div class="search">What Are You looking For?
      <svg width="10" height="10" viewBox="0 0 10 10"><circle cx="4.2" cy="4.2" r="3.2" fill="none" stroke="#111" stroke-width="1"/><line x1="6.6" y1="6.6" x2="9.2" y2="9.2" stroke="#111" stroke-width="1.1"/></svg>
    </div>
    <div class="account">SIGN IN/ MY ACCOUNT</div>
    <svg class="account-icon" width="8" height="8" viewBox="0 0 8 8"><circle cx="4" cy="2.2" r="2" fill="#111"/><path d="M0.5 8 Q4 3.8 7.5 8Z" fill="#111"/></svg>
    <svg class="bag-icon" width="7" height="8" viewBox="0 0 7 8"><rect x="0" y="2" width="7" height="6" rx="1" fill="#111"/><path d="M2 3V1.5a1.5 1.5 0 0 1 3 0V3" fill="none" stroke="#fff" stroke-width="0.7"/></svg>
    <nav class="nav"><a>HOME &amp; GARDEN</a><a>SPORT &amp; FITNESS</a><a>PETS</a><a>KIDS</a><a>BABIES</a><a>MEN</a><a>WOMEN</a><a>GIFTS</a><a>NEW</a></nav>
  </header>
  <div class="hero">
    <div class="hero-card">
      <div class="hero-photo" role="img" aria-label="Photo of a potted snake plant in a white pot"></div>
      <h1 class="hero-title">5 Fake Houseplants<br><em>For</em> the Criminally<br>Negligent</h1>
      <div class="hero-btn">SHOW ME!</div>
    </div>
    <div class="tile t1" role="img" aria-label="Photo of a leafy houseplant in a cream pot"></div>
    <div class="tile t2" role="img" aria-label="Photo of a broad-leaf plant in a beige pot"></div>
    <div class="tile t3" role="img" aria-label="Photo of a small plant in a white pot"></div>
    <div class="tile t4" role="img" aria-label="Photo of a spiky plant in a stone pot"></div>
  </div>
  <h2 class="section-title">Recent Additions</h2>
  <svg class="pager prev" width="9" height="7" viewBox="0 0 9 7"><path d="M8.5 3.5H1M3.5 0.8 0.8 3.5 3.5 6.2" fill="none" stroke="#e93a3a" stroke-width="1.2"/></svg>
  <svg class="pager next" width="9" height="7" viewBox="0 0 9 7"><path d="M0.5 3.5H8M5.5 0.8 8.2 3.5 5.5 6.2" fill="none" stroke="#999" stroke-width="1.2"/></svg>
  <article class="mini-card c1"><div class="mini-img" role="img" aria-label="Photo of a black portable charger"></div><p class="mini-text">5 portable chargers FOR when mum needs a quick chat</p></article>
  <article class="mini-card c2"><div class="mini-img" role="img" aria-label="Photo of a dog collar"></div><div class="quick-view">VIEW MORE</div><div class="quick-cart">ADD TO CART</div><p class="mini-text">5 brilliant collars FOR budget conscious border collies</p></article>
  <article class="mini-card c3"><div class="mini-img" role="img" aria-label="Photo of a slate cheese board"></div><p class="mini-text">5 cheese boards FOR asiago aficionados</p></article>
  <div class="view-more">View More</div>
  <aside class="flash">
    <div class="flash-img" role="img" aria-label="Photo of a smart doorbell camera, chime and charging stand"></div>
    <div class="flash-title">Flash Deals</div>
    <div class="flash-sub">Up to 65% off</div>
  </aside>
  <footer class="site-footer">
    <div class="brand">3Loom</div>
    <div class="footer-links">About Us<span>|</span>FAQ<span>|</span>Contact US<span>|</span>Terms of Service<span>|</span>Return Policy<span>|</span>Shipping Policy<span>|</span>Track My Order</div>
    <div class="socials"><i></i><i></i><i></i><i></i><i></i></div>
  </footer>
  <div class="copyright">©Copyrights 2024 3Loom &nbsp;|&nbsp; All Rights Reserved</div>
</section>

<!-- Layout B -->
<section class="page page--b">
  <header class="site-header">
    <div class="brand">3Loom</div>
    <div class="search">What Are You looking For?
      <svg width="10" height="10" viewBox="0 0 10 10"><circle cx="4.2" cy="4.2" r="3.2" fill="none" stroke="#111" stroke-width="1"/><line x1="6.6" y1="6.6" x2="9.2" y2="9.2" stroke="#111" stroke-width="1.1"/></svg>
    </div>
    <div class="account">SIGN IN/ MY ACCOUNT</div>
    <svg class="account-icon" width="8" height="8" viewBox="0 0 8 8"><circle cx="4" cy="2.2" r="2" fill="#111"/><path d="M0.5 8 Q4 3.8 7.5 8Z" fill="#111"/></svg>
    <svg class="bag-icon" width="7" height="8" viewBox="0 0 7 8"><rect x="0" y="2" width="7" height="6" rx="1" fill="#111"/><path d="M2 3V1.5a1.5 1.5 0 0 1 3 0V3" fill="none" stroke="#fff" stroke-width="0.7"/></svg>
    <nav class="nav"><a>HOME &amp; GARDEN</a><a>SPORT &amp; FITNESS</a><a>PETS</a><a>KIDS</a><a>BABIES</a><a>MEN</a><a>WOMEN</a><a>GIFTS</a><a>NEW</a></nav>
  </header>
  <div class="hero">
    <div class="hero-card">
      <div class="hero-photo" role="img" aria-label="Photo of a potted snake plant in a white pot"></div>
      <h1 class="hero-title">5 Fake Houseplants<br><em>For</em> the Criminally<br>Negligent</h1>
      <div class="hero-btn">SHOW ME!</div>
    </div>
    <div class="tile t1" role="img" aria-label="Photo of a leafy houseplant in a cream pot"></div>
    <div class="tile t2" role="img" aria-label="Photo of a broad-leaf plant in a beige pot"></div>
    <div class="tile t3" role="img" aria-label="Photo of a small plant in a white pot"></div>
    <div class="tile t4" role="img" aria-label="Photo of a spiky plant in a stone pot"></div>
  </div>
  <h2 class="section-title">Recent Additions</h2>
  <div class="feature-arrow left"><svg width="8" height="10" viewBox="0 0 8 10"><path d="M6 1 2 5 6 9" fill="none" stroke="#fff" stroke-width="1.6"/></svg></div>
  <div class="feature-arrow right"><svg width="8" height="10" viewBox="0 0 8 10"><path d="M2 1 6 5 2 9" fill="none" stroke="#fff" stroke-width="1.6"/></svg></div>
  <article class="feature f1" role="img" aria-label="Photo of a white power bank"><h3 class="feature-title">5 Portable Chargers FOR When Mum Needs A Quick Chat</h3></article>
  <article class="feature f2" role="img" aria-label="Photo of a red glitter dog collar"><h3 class="feature-title">5 Brilliant Collars FOR Budget Conscious Border Collies</h3></article>
  <article class="feature f3" role="img" aria-label="Photo of colourful sensory toys"><h3 class="feature-title">5 Sensory Toys FOR Babies That Are Easily Amazed</h3></article>
  <aside class="arrivals">
    <div class="arrivals-img" role="img" aria-label="Photo of a phone on a wireless charging stand"></div>
    <div class="arrivals-title">NEW ARRIVALS</div>
    <div class="arrivals-sub">BEAUTY, DECOR &amp; MORE.</div>
    <p class="arrivals-copy">Lorem ipsum dolor sit amet, consectetur adipiscing elit, sed do eiusmod tempor incididunt ut labore et dolore magna aliqua. Quis ipsum suspendisse ultrices gravida. Risus commodo viverra maecenas accumsan lacus vel facilisis.</p>
    <div class="arrivals-btn">SHOP NOW</div>
  </aside>
  <footer class="site-footer">
    <div class="brand">3Loom</div>
    <div class="footer-links">About Us<span>|</span>FAQ<span>|</span>Contact US<span>|</span>Terms of Service<span>|</span>Return Policy<span>|</span>Shipping Policy<span>|</span>Track My Order</div>
    <div class="socials"><i></i><i></i><i></i><i></i><i></i></div>
  </footer>
  <div class="copyright">©Copyrights 2024 3Loom &nbsp;|&nbsp; All Rights Reserved</div>
</section>

</body>
</html>
```